Online Course Page

We are building a video based online course page. This project is for only the actual page that the student will watch the videos at. They will watch one vide at a time. Once one video lesson is completed then they can move to the next video lesson. The page will need to show the video player. (Main feature.) The list of lessons in the course. Instructor information. Profile picture and bio of the instructor. A Live chat button that will initiate a chat in real-time with the instructor.

The winning designer will also be asked to to design the dashboard area and other aspects of the user interface as an additional project.

Target Market(s)

Adults

Number of Pages Required

1 page

Colors
9bcb3c

Requirements
Must have
• Our logo is attached. Green and grey are our colors. Should feel modern, clean and be simple to navigate. The site will be responsive so the layout should work well on mobile devices.

```html
<!DOCTYPE html>
<html lang="en">
<head>
<meta charset="utf-8">
<title>CourseHaven – Course Player</title>
<link rel="stylesheet" href="https://fonts.googleapis.com/css2?family=Montserrat:wght@300;400;500&family=Open+Sans:wght@300;400;600;700&display=swap">
<style>
:root{
  --green:#8bc34a;
  --green-deep:#5fa336;
  --green-hero-a:#86c95e;
  --green-hero-b:#5ea83c;
  --green-pale:#e1eed4;
  --teal:#45d0c1;
  --paper:#f3f3f3;
  --ink:#1d1d1d;
  --night:#17191c;
  --white:#ffffff;
  --star:#f7c21b;
}
*{margin:0;padding:0;box-sizing:border-box}
html,body{width:945px;height:1200px;overflow:hidden}
body{position:relative;background:var(--paper);font-family:"Open Sans",sans-serif;color:var(--ink)}
.abs{position:absolute}

/* hero */
.hero{left:0;top:0;width:945px;height:346px;background:linear-gradient(120deg,var(--green-hero-a) 0%,#73bb4f 50%,var(--green-hero-b) 100%);overflow:hidden}
.logo-tab{left:105px;top:0;width:131px;height:116px;background:var(--white);border-radius:0 0 16px 16px;display:flex;align-items:center;justify-content:center;gap:6px}
.logo-dot{width:12px;height:12px;border-radius:50%;background:var(--green)}
.logo-name{font-family:"Open Sans",sans-serif;font-weight:600;font-size:14px;color:var(--green-deep)}
.hero-title{left:213px;top:148px;font-family:"Montserrat",sans-serif;font-weight:300;font-size:34px;color:var(--white);letter-spacing:.5px;line-height:1}
.hero-sub{left:215px;top:179px;font-weight:600;font-size:11.5px;color:var(--white);letter-spacing:.1px}
.btn-signup{left:302px;top:201px;width:97px;height:18px;background:var(--teal);color:var(--white);font-weight:600;font-size:10.5px;display:flex;align-items:center;justify-content:center}
.hero-visual{left:485px;top:52px;width:295px;height:296px;border-radius:10px;background:linear-gradient(160deg,#e9e9e9 0%,#d3d3d3 60%,rgba(210,210,210,.4) 100%)}

/* course section */
.blob{border-radius:50%;background:var(--green-pale)}
.section-title{left:0;top:398px;width:975px;text-align:center;font-family:"Montserrat",sans-serif;font-weight:400;font-size:19px;letter-spacing:.3px}
.section-tag{left:0;top:422px;width:975px;text-align:center;font-size:11px;color:var(--teal);letter-spacing:.5px}
.player-screen{left:98px;top:471px;width:387px;height:256px;background:linear-gradient(135deg,#4a3f33 0%,#6b5b49 45%,#3a332c 100%)}
.player-caption{left:98px;top:570px;width:410px;text-align:center;font-family:"Open Sans",sans-serif;font-weight:400;font-size:37px;line-height:.9;color:var(--white)}
.player-controls{left:98px;top:727px;width:387px;height:30px;background:#e6e6e6}
.lesson-title{left:515px;top:482px;font-family:"Montserrat",sans-serif;font-weight:400;font-size:16px;color:var(--green-deep);letter-spacing:.3px}
.lesson-text{left:540px;top:507px;width:320px;font-size:9.5px;line-height:11.5px}
.lesson-text p{margin-bottom:5px}
.info-band{left:485px;top:727px;width:460px;height:30px;background:var(--green)}
.band-left{left:0;top:727px;width:98px;height:30px;background:var(--green)}
.band-label{left:499px;top:741px;font-weight:700;font-size:8.5px;color:var(--white)}
.band-label span{text-decoration:underline}

/* instructor */
.instructor{left:0;top:757px;width:945px;height:366px;background:linear-gradient(120deg,#22262b 0%,var(--night) 45%,#2a2824 100%)}
.kicker{left:0;top:777px;width:945px;text-align:center;font-family:"Montserrat",sans-serif;font-size:15px;color:var(--white)}
.instructor-heading{left:0;top:792px;width:945px;text-align:center;font-family:"Montserrat",sans-serif;font-size:25px;color:var(--white);letter-spacing:.5px}
.instructor-name{left:0;top:1016px;width:945px;text-align:center;font-family:"Montserrat",sans-serif;color:var(--white)}
.instructor-name .first{font-size:17px}
.instructor-name .last{font-size:25px}
.instructor-bio{left:235px;top:1050px;width:475px;text-align:center;font-size:9.5px;line-height:11.5px;color:var(--white)}
.more-link{left:0;top:1094px;width:930px;text-align:center;font-size:9px;color:var(--green);text-decoration:underline}

/* footer */
.social{left:0;top:1137px;width:945px;display:flex;justify-content:center;gap:12px}
.social span{width:18px;height:18px;border-radius:50%;background:var(--ink)}
.copyright{left:0;top:1169px;width:930px;text-align:center;font-size:9px}
</style>
</head>
<body>

<header class="abs hero">
  <div class="abs hero-visual" role="img" aria-label="Desktop computer showing the course website"></div>
</header>
<div class="abs logo-tab"><span class="logo-dot"></span><span class="logo-name">CourseHaven</span></div>
<h1 class="abs hero-title">WE CARE</h1>
<p class="abs hero-sub">ABOUT YOUR UPCOMING COURSES</p>
<a class="abs btn-signup">SIGN UP NOW</a>

<div class="abs blob" style="left:84px;top:353px;width:120px;height:60px"></div>
<div class="abs blob" style="left:212px;top:353px;width:96px;height:48px"></div>
<div class="abs blob" style="left:4px;top:421px;width:156px;height:80px"></div>
<div class="abs blob" style="left:84px;top:530px;width:60px;height:80px"></div>

<h2 class="abs section-title">NAME OF COURSE RIGHT NOW</h2>
<p class="abs section-tag">SECTION 2</p>

<div class="abs player-screen" role="img" aria-label="Video frame: desk from above with papers, plant and laptop"></div>
<p class="abs player-caption">sculpt<br>course</p>
<div class="abs player-controls">
  <svg width="387" height="30" viewBox="0 0 387 30">
    <rect x="40" y="10" width="2.5" height="9" fill="#111"/><rect x="44.5" y="10" width="2.5" height="9" fill="#111"/>
    <path d="M65 9.5 L74 14.5 L65 19.5Z" fill="#111"/>
    <rect x="91" y="10" width="9" height="9" fill="#111"/>
    <path d="M334 12v-3h3M341 9h3v3M344 17v3h-3M337 20h-3v-3" stroke="#111" stroke-width="1.5" fill="none"/>
    <path d="M363 11a5 5 0 1 0 1.5 4" stroke="#111" stroke-width="2" fill="none"/>
    <path d="M360 8l4.5 2.5-3.8 3z" fill="#111"/>
  </svg>
</div>

<h3 class="abs lesson-title">01. NAME OF ACTIVATED VIDEO</h3>
<div class="abs lesson-text">
  <p>Descraption of the video which is playing now Note that the video can play as full screen by the build in icon in video player</p>
  <p>Now Note that the video can play as full screen by the build in icon in video player</p>
  <p>Now Note that the video can play as full screen by the build in icon in video player</p>
</div>

<div class="abs band-left"></div>
<div class="abs info-band">
  <svg class="abs" style="left:347px;top:6px" width="22" height="18" viewBox="0 0 22 18">
    <circle cx="2" cy="3" r="2" fill="#fff"/><rect x="6" y="1.5" width="16" height="3" rx="1.5" fill="#fff"/>
    <circle cx="2" cy="9" r="2" fill="#fff"/><rect x="6" y="7.5" width="16" height="3" rx="1.5" fill="#fff"/>
    <circle cx="2" cy="15" r="2" fill="#fff"/><rect x="6" y="13.5" width="16" height="3" rx="1.5" fill="#fff"/>
  </svg>
</div>
<p class="abs band-label">INESTRACTOR: <span>SAM HARLOW</span></p>

<section class="abs instructor" role="img" aria-label="Dimmed photo of a team working at a table"></section>
<p class="abs kicker">to Know the</p>
<h2 class="abs instructor-heading">INESTRACTOR</h2>
<svg class="abs" style="left:385px;top:815px" width="175" height="160" viewBox="0 0 175 160">
  <circle cx="87" cy="2" r="1.5" fill="#fff"/>
  <circle cx="8" cy="88" r="2" fill="#fff"/>
  <circle cx="164" cy="88" r="2" fill="#fff"/>
  <polygon points="87,20 145,52 145,117 87,152 29,117 29,52" fill="#b9b2a8" stroke="#e8e8e8" stroke-width="3" stroke-linejoin="round" role="img" aria-label="Instructor portrait"/>
</svg>
<svg class="abs" style="left:422px;top:975px" width="100" height="32" viewBox="0 0 100 32">
  <g fill="var(--star)">
    <polygon points="16,2 20,12 31,12 22,19 25,30 16,23 7,30 10,19 1,12 12,12"/>
    <polygon points="50,2 54,12 65,12 56,19 59,30 50,23 41,30 44,19 35,12 46,12"/>
    <polygon points="84,2 88,12 99,12 90,19 93,30 84,23 75,30 78,19 69,12 80,12"/>
  </g>
</svg>
<p class="abs instructor-name"><span class="first">Sam </span><span class="last">HARLOW</span></p>
<p class="abs instructor-bio">Descraption of the video which is playing now Note that the video can play as full screen by the build in icon in video player Descraption of the video which is playing now Note that the video can play as full screen by the build in icon in video player</p>
<a class="abs more-link">like to know other inestractors</a>

<nav class="abs social" aria-label="Social links">
  <span></span><span></span><span></span><span></span><span></span><span></span>
</nav>
<p class="abs copyright">All copyrights reseerved by yourcompnay @2018</p>

</body>
</html>
```